Design für einen Jahresplaner gesucht
Zielgruppe
Scannen und Designen Zahntechnischer und Zahnmedizinischer Arbeiten und das Fräsen und 3d Drucken von bereits in CAD konstruierten Objekten. Wir verfügen über die modernsten Zahntechnischen Technologien und bieten diese als Dienstleister für Dentallabore an.
Aufgabenstellung
Wir benotigen ein Jahresplaner für unsere Kunden. Die Beigefügte Vorlage dient regelrecht nur der Grösenvorlage.
Das Design soll Technisch und Innovativ sein. Gleischzeitig aber gradlinig und nicht zu verspielt.
Das Logo kann ruhig stark ins Auge fallen. Die Schriftfarben sollen überwigen dunkelgrau sein. Hervorzuhebende Bereiche wie z. B. Sonntage, Feiertage sollten die Logofaben beinhalten. Bilder können auch verwendet werden aber wir würden uns über ein Schönes Layout ohne Bilder auch freuen.
PS: Unter dem Logo muss in Feiner Schrift stehen
eine Marke der Norvak GmbH

```html
<!DOCTYPE html>
<html lang="de">
<head>
<meta charset="utf-8">
<title>Jahresplaner 2019 – Fravex</title>
<link href="https://fonts.googleapis.com/css2?family=Poppins:wght@400;500;600&family=Arimo&display=swap" rel="stylesheet">
<style>
:root{
  --stage:#e4e4e4;
  --paper:#efefef;
  --white:#ffffff;
  --ink:#333333;
  --ink-soft:#666666;
  --accent:#e23b3f;
  --blue:#29a3dd;
  --bar:#cfcfcf;
  --dark:#2a2a2a;
}
*{margin:0;padding:0;box-sizing:border-box}
html,body{width:1200px;height:1200px;overflow:hidden;background:var(--stage)}
body{font-family:"Poppins",sans-serif;color:var(--ink)}
.planner{position:absolute;left:0;top:180px;width:1200px;height:840px;background:var(--paper);overflow:hidden}
.header{position:absolute;left:0;top:0;width:1200px;height:144px;background:linear-gradient(90deg,#e9e9e9,#dcdcdc)}
.header svg{position:absolute;left:0;top:0}
.brand{position:absolute;left:22px;top:24px;width:220px;height:80px}
.brand-dot{position:absolute;left:0;top:6px;width:34px;height:34px;border-radius:50%;background:var(--blue)}
.brand-name{position:absolute;left:46px;top:2px;font-size:31px;font-weight:600;color:#555;letter-spacing:.5px}
.brand-sub{position:absolute;left:72px;top:53px;font-size:11px;letter-spacing:2.6px;color:#555;font-weight:400}
.contact{position:absolute;top:104px;height:22px;display:flex;align-items:center;font-family:"Arimo",sans-serif;font-size:17px;color:#555}
.contact .icon{width:22px;height:22px;background:var(--blue);display:flex;align-items:center;justify-content:center;margin-right:14px}
.band{position:absolute;left:0;top:144px;width:1200px;height:21px;background:var(--blue)}
.band span{position:absolute;top:2px;font-size:12.5px;color:var(--white);font-weight:500}
.month{position:absolute;top:176px;list-style:none}
.month li{height:19.13px;font-size:9.5px;display:flex;align-items:center;white-space:nowrap}
.month li b{font-weight:400;width:16px}
.month li em{font-style:normal;width:19px}
.month li i{font-style:normal;font-size:4.6px;line-height:1.15;color:var(--ink);width:42px;white-space:normal}
.month li.r{color:var(--accent)}
.note{position:absolute;top:775px;font-size:4.6px;line-height:1.5;color:var(--ink-soft)}
</style>
</head>
<body>
<div class="planner">
  <header class="header">
    <svg width="1200" height="144" viewBox="0 0 1200 144">
      <rect x="290" y="0" width="420" height="100" fill="#e3e3e3" role="img" aria-label="Fotos von Dental-Abutments aus Titan, Gold und Keramik"/>
      <polygon points="0,0 248,0 248,100 218,121 0,121" fill="var(--white)"/>
      <polygon points="622,28 700,0 1200,0 1200,144 1020,144" fill="#c9c9c9"/>
      <polygon points="640,42 742,0 1200,0 1200,144 1010,144" fill="url(#photo)" role="img" aria-label="Schwarzweißfoto einer gefrästen Implantatbrücke aus Metall"/>
      <polygon points="286,99 1060,99 1120,131 266,131" fill="var(--bar)"/>
      <defs>
        <linearGradient id="photo" x1="0" y1="0" x2="1" y2="1">
          <stop offset="0" stop-color="#9a9a9a"/>
          <stop offset=".45" stop-color="#5a5a5a"/>
          <stop offset="1" stop-color="#1e1e1e"/>
        </linearGradient>
      </defs>
    </svg>
    <div class="brand">
      <div class="brand-dot"></div>
      <div class="brand-name">Fravex</div>
      <div class="brand-sub">Norvak GmbH</div>
    </div>
    <div class="contact" style="left:313px"><span class="icon"><svg width="12" height="12" viewBox="0 0 24 24"><path fill="#fff" d="M6.6 10.8a15 15 0 0 0 6.6 6.6l2.2-2.2c.3-.3.7-.4 1-.2 1.1.4 2.3.6 3.6.6.6 0 1 .4 1 1V20c0 .6-.4 1-1 1A17 17 0 0 1 3 4c0-.6.4-1 1-1h3.5c.6 0 1 .4 1 1 0 1.3.2 2.5.6 3.6.1.3 0 .7-.2 1z"/></svg></span>0228-4417390</div>
    <div class="contact" style="left:490px"><span class="icon"><svg width="12" height="12" viewBox="0 0 24 24"><path fill="#fff" d="M6 3h12v5H6zM4 9h16a2 2 0 0 1 2 2v6h-4v4H6v-4H2v-6a2 2 0 0 1 2-2zm4 7v3h8v-3z"/></svg></span>0228-441739-21</div>
    <div class="contact" style="left:681px"><span class="icon"><svg width="13" height="13" viewBox="0 0 24 24" fill="none" stroke="#fff" stroke-width="1.8"><circle cx="12" cy="12" r="9"/><path d="M3 12h18M12 3c3 3 3 15 0 18M12 3c-3 3-3 15 0 18"/></svg></span>www.fravex-dental.de</div>
  </header>

  <div class="band">
    <span style="left:39px">Januar</span><span style="left:124px">Februar</span><span style="left:209px">März</span><span style="left:294px">April</span><span style="left:379px">Mai</span><span style="left:464px">Juni</span><span style="left:549px">Juli</span><span style="left:634px">August</span><span style="left:719px">September</span><span style="left:804px">Oktober</span><span style="left:890px">November</span><span style="left:974px">Dezember</span><span style="left:1075px">Januar 2020</span>
  </div>

  <ul class="month" style="left:43px">
    <li class="r"><b>01</b><em>Di</em><i>Neujahr</i></li><li><b>02</b><em>Mi</em></li><li><b>03</b><em>Do</em></li><li><b>04</b><em>Fr</em></li><li class="r"><b>05</b><em>Sa</em></li><li class="r"><b>06</b><em>So</em><i>Heilige Drei Könige*</i></li>
    <li><b>07</b><em>Mo</em></li><li><b>08</b><em>Di</em></li><li><b>09</b><em>Mi</em></li><li><b>10</b><em>Do</em></li><li><b>11</b><em>Fr</em></li><li class="r"><b>12</b><em>Sa</em></li><li class="r"><b>13</b><em>So</em></li>
    <li><b>14</b><em>Mo</em></li><li><b>15</b><em>Di</em></li><li><b>16</b><em>Mi</em></li><li><b>17</b><em>Do</em></li><li><b>18</b><em>Fr</em></li><li class="r"><b>19</b><em>Sa</em></li><li class="r"><b>20</b><em>So</em></li>
    <li><b>21</b><em>Mo</em></li><li><b>22</b><em>Di</em></li><li><b>23</b><em>Mi</em></li><li><b>24</b><em>Do</em></li><li><b>25</b><em>Fr</em></li><li class="r"><b>26</b><em>Sa</em></li><li class="r"><b>27</b><em>So</em></li>
    <li><b>28</b><em>Mo</em></li><li><b>29</b><em>Di</em></li><li><b>30</b><em>Mi</em></li><li><b>31</b><em>Do</em></li>
  </ul>
  <ul class="month" style="left:128px">
    <li><b>01</b><em>Fr</em></li><li class="r"><b>02</b><em>Sa</em></li><li class="r"><b>03</b><em>So</em></li>
    <li><b>04</b><em>Mo</em></li><li><b>05</b><em>Di</em></li><li><b>06</b><em>Mi</em></li><li><b>07</b><em>Do</em></li><li><b>08</b><em>Fr</em></li><li class="r"><b>09</b><em>Sa</em></li><li class="r"><b>10</b><em>So</em></li>
    <li><b>11</b><em>Mo</em></li><li><b>12</b><em>Di</em></li><li><b>13</b><em>Mi</em></li><li><b>14</b><em>Do</em><i>Valentinstag</i></li><li><b>15</b><em>Fr</em></li><li class="r"><b>16</b><em>Sa</em></li><li class="r"><b>17</b><em>So</em></li>
    <li><b>18</b><em>Mo</em></li><li><b>19</b><em>Di</em></li><li><b>20</b><em>Mi</em></li><li><b>21</b><em>Do</em></li><li><b>22</b><em>Fr</em></li><li class="r"><b>23</b><em>Sa</em></li><li class="r"><b>24</b><em>So</em></li>
    <li><b>25</b><em>Mo</em></li><li><b>26</b><em>Di</em></li><li><b>27</b><em>Mi</em></li><li><b>28</b><em>Do</em></li>
  </ul>
  <ul class="month" style="left:213px">
    <li><b>01</b><em>Fr</em></li><li class="r"><b>02</b><em>Sa</em></li><li class="r"><b>03</b><em>So</em></li>
    <li><b>04</b><em>Mo</em><i>Rosenmontag</i></li><li><b>05</b><em>Di</em><i>Fastnacht</i></li><li><b>06</b><em>Mi</em><i>Ascher­mittwoch</i></li><li><b>07</b><em>Do</em></li><li><b>08</b><em>Fr</em></li><li class="r"><b>09</b><em>Sa</em></li><li class="r"><b>10</b><em>So</em></li>
    <li><b>11</b><em>Mo</em></li><li><b>12</b><em>Di</em></li><li><b>13</b><em>Mi</em></li><li><b>14</b><em>Do</em></li><li><b>15</b><em>Fr</em></li><li class="r"><b>16</b><em>Sa</em></li><li class="r"><b>17</b><em>So</em></li>
    <li><b>18</b><em>Mo</em></li><li><b>19</b><em>Di</em></li><li><b>20</b><em>Mi</em></li><li><b>21</b><em>Do</em></li><li><b>22</b><em>Fr</em></li><li class="r"><b>23</b><em>Sa</em></li><li class="r"><b>24</b><em>So</em></li>
    <li><b>25</b><em>Mo</em></li><li><b>26</b><em>Di</em></li><li><b>27</b><em>Mi</em></li><li><b>28</b><em>Do</em></li><li><b>29</b><em>Fr</em></li><li class="r"><b>30</b><em>Sa</em></li><li class="r"><b>31</b><em>So</em><i>Beginn der Sommerzeit</i></li>
  </ul>
  <ul class="month" style="left:298px">
    <li><b>01</b><em>Mo</em></li><li><b>02</b><em>Di</em></li><li><b>03</b><em>Mi</em></li><li><b>04</b><em>Do</em></li><li><b>05</b><em>Fr</em></li><li class="r"><b>06</b><em>Sa</em></li><li class="r"><b>07</b><em>So</em></li>
    <li><b>08</b><em>Mo</em></li><li><b>09</b><em>Di</em></li><li><b>10</b><em>Mi</em></li><li><b>11</b><em>Do</em></li><li><b>12</b><em>Fr</em></li><li class="r"><b>13</b><em>Sa</em></li><li class="r"><b>14</b><em>So</em><i>Palmsonntag</i></li>
    <li><b>15</b><em>Mo</em></li><li><b>16</b><em>Di</em></li><li><b>17</b><em>Mi</em></li><li><b>18</b><em>Do</em><i>Grün­donnerstag</i></li><li class="r"><b>19</b><em>Fr</em><i>Karfreitag</i></li><li class="r"><b>20</b><em>Sa</em><i>Karsamstag</i></li><li class="r"><b>21</b><em>So</em><i>Ostersonntag</i></li>
    <li class="r"><b>22</b><em>Mo</em><i>Ostermontag</i></li><li><b>23</b><em>Di</em></li><li><b>24</b><em>Mi</em></li><li><b>25</b><em>Do</em></li><li><b>26</b><em>Fr</em></li><li class="r"><b>27</b><em>Sa</em></li><li class="r"><b>28</b><em>So</em></li>
    <li><b>29</b><em>Mo</em></li><li><b>30</b><em>Di</em><i>Walpurgis­nacht</i></li>
  </ul>
  <ul class="month" style="left:383px">
    <li class="r"><b>01</b><em>Mi</em><i>Tag der Arbeit</i></li><li><b>02</b><em>Do</em></li><li><b>03</b><em>Fr</em></li><li class="r"><b>04</b><em>Sa</em></li><li class="r"><b>05</b><em>So</em></li>
    <li><b>06</b><em>Mo</em></li><li><b>07</b><em>Di</em></li><li><b>08</b><em>Mi</em></li><li><b>09</b><em>Do</em></li><li><b>10</b><em>Fr</em></li><li class="r"><b>11</b><em>Sa</em></li><li class="r"><b>12</b><em>So</em><i>Muttertag</i></li>
    <li><b>13</b><em>Mo</em></li><li><b>14</b><em>Di</em></li><li><b>15</b><em>Mi</em></li><li><b>16</b><em>Do</em></li><li><b>17</b><em>Fr</em></li><li class="r"><b>18</b><em>Sa</em></li><li class="r"><b>19</b><em>So</em></li>
    <li><b>20</b><em>Mo</em></li><li><b>21</b><em>Di</em></li><li><b>22</b><em>Mi</em></li><li><b>23</b><em>Do</em></li><li><b>24</b><em>Fr</em></li><li class="r"><b>25</b><em>Sa</em></li><li class="r"><b>26</b><em>So</em></li>
    <li><b>27</b><em>Mo</em></li><li><b>28</b><em>Di</em></li><li><b>29</b><em>Mi</em></li><li class="r"><b>30</b><em>Do</em><i>Christi Himmelfahrt</i></li><li><b>31</b><em>Fr</em></li>
  </ul>
  <ul class="month" style="left:468px">
    <li class="r"><b>01</b><em>Sa</em></li><li class="r"><b>02</b><em>So</em></li>
    <li><b>03</b><em>Mo</em></li><li><b>04</b><em>Di</em></li><li><b>05</b><em>Mi</em></li><li><b>06</b><em>Do</em></li><li><b>07</b><em>Fr</em></li><li class="r"><b>08</b><em>Sa</em></li><li class="r"><b>09</b><em>So</em><i>Pfingst­sonntag</i></li>
    <li class="r"><b>10</b><em>Mo</em><i>Pfingst­montag</i></li><li><b>11</b><em>Di</em></li><li><b>12</b><em>Mi</em></li><li><b>13</b><em>Do</em></li><li><b>14</b><em>Fr</em></li><li class="r"><b>15</b><em>Sa</em></li><li class="r"><b>16</b><em>So</em></li>
    <li><b>17</b><em>Mo</em></li><li><b>18</b><em>Di</em></li><li><b>19</b><em>Mi</em></li><li class="r"><b>20</b><em>Do</em><i>Fronleichnam*</i></li><li><b>21</b><em>Fr</em></li><li class="r"><b>22</b><em>Sa</em></li><li class="r"><b>23</b><em>So</em></li>
    <li><b>24</b><em>Mo</em><i>Johannistag</i></li><li><b>25</b><em>Di</em></li><li><b>26</b><em>Mi</em></li><li><b>27</b><em>Do</em></li><li><b>28</b><em>Fr</em></li><li class="r"><b>29</b><em>Sa</em><i>Peter und Paul</i></li><li class="r"><b>30</b><em>So</em></li>
  </ul>
  <ul class="month" style="left:553px">
    <li><b>01</b><em>Mo</em></li><li><b>02</b><em>Di</em></li><li><b>03</b><em>Mi</em></li><li><b>04</b><em>Do</em></li><li><b>05</b><em>Fr</em></li><li class="r"><b>06</b><em>Sa</em></li><li class="r"><b>07</b><em>So</em></li>
    <li><b>08</b><em>Mo</em></li><li><b>09</b><em>Di</em></li><li><b>10</b><em>Mi</em></li><li><b>11</b><em>Do</em></li><li><b>12</b><em>Fr</em></li><li class="r"><b>13</b><em>Sa</em></li><li class="r"><b>14</b><em>So</em></li>
    <li><b>15</b><em>Mo</em></li><li><b>16</b><em>Di</em></li><li><b>17</b><em>Mi</em></li><li><b>18</b><em>Do</em></li><li><b>19</b><em>Fr</em></li><li class="r"><b>20</b><em>Sa</em></li><li class="r"><b>21</b><em>So</em></li>
    <li><b>22</b><em>Mo</em></li><li><b>23</b><em>Di</em></li><li><b>24</b><em>Mi</em></li><li><b>25</b><em>Do</em></li><li><b>26</b><em>Fr</em></li><li class="r"><b>27</b><em>Sa</em></li><li class="r"><b>28</b><em>So</em></li>
    <li><b>29</b><em>Mo</em></li><li><b>30</b><em>Di</em></li><li><b>31</b><em>Mi</em></li>
  </ul>
  <ul class="month" style="left:638px">
    <li><b>01</b><em>Do</em></li><li><b>02</b><em>Fr</em></li><li class="r"><b>03</b><em>Sa</em></li><li class="r"><b>04</b><em>So</em></li>
    <li><b>05</b><em>Mo</em></li><li><b>06</b><em>Di</em></li><li><b>07</b><em>Mi</em></li><li><b>08</b><em>Do</em></li><li><b>09</b><em>Fr</em></li><li class="r"><b>10</b><em>Sa</em></li><li class="r"><b>11</b><em>So</em></li>
    <li><b>12</b><em>Mo</em></li><li><b>13</b><em>Di</em></li><li><b>14</b><em>Mi</em></li><li class="r"><b>15</b><em>Do</em><i>Mariä Himmelfahrt*</i></li><li><b>16</b><em>Fr</em></li><li class="r"><b>17</b><em>Sa</em></li><li class="r"><b>18</b><em>So</em></li>
    <li><b>19</b><em>Mo</em></li><li><b>20</b><em>Di</em></li><li><b>21</b><em>Mi</em></li><li><b>22</b><em>Do</em></li><li><b>23</b><em>Fr</em></li><li class="r"><b>24</b><em>Sa</em></li><li class="r"><b>25</b><em>So</em></li>
    <li><b>26</b><em>Mo</em></li><li><b>27</b><em>Di</em></li><li><b>28</b><em>Mi</em></li><li><b>29</b><em>Do</em></li><li><b>30</b><em>Fr</em></li><li class="r"><b>31</b><em>Sa</em></li>
  </ul>
  <ul class="month" style="left:723px">
    <li class="r"><b>01</b><em>So</em></li>
    <li><b>02</b><em>Mo</em></li><li><b>03</b><em>Di</em></li><li><b>04</b><em>Mi</em></li><li><b>05</b><em>Do</em></li><li><b>06</b><em>Fr</em></li><li class="r"><b>07</b><em>Sa</em></li><li class="r"><b>08</b><em>So</em></li>
    <li><b>09</b><em>Mo</em></li><li><b>10</b><em>Di</em></li><li><b>11</b><em>Mi</em></li><li><b>12</b><em>Do</em></li><li><b>13</b><em>Fr</em></li><li class="r"><b>14</b><em>Sa</em></li><li class="r"><b>15</b><em>So</em></li>
    <li><b>16</b><em>Mo</em></li><li><b>17</b><em>Di</em></li><li><b>18</b><em>Mi</em></li><li><b>19</b><em>Do</em></li><li><b>20</b><em>Fr</em></li><li class="r"><b>21</b><em>Sa</em></li><li class="r"><b>22</b><em>So</em></li>
    <li><b>23</b><em>Mo</em></li><li><b>24</b><em>Di</em></li><li><b>25</b><em>Mi</em></li><li><b>26</b><em>Do</em></li><li><b>27</b><em>Fr</em></li><li class="r"><b>28</b><em>Sa</em></li><li class="r"><b>29</b><em>So</em></li>
    <li><b>30</b><em>Mo</em></li>
  </ul>
  <ul class="month" style="left:808px">
    <li><b>01</b><em>Di</em></li><li><b>02</b><em>Mi</em></li><li class="r"><b>03</b><em>Do</em><i>Tag der Deutschen Einheit</i></li><li><b>04</b><em>Fr</em></li><li class="r"><b>05</b><em>Sa</em></li><li class="r"><b>06</b><em>So</em><i>Erntedankfest</i></li>
    <li><b>07</b><em>Mo</em></li><li><b>08</b><em>Di</em></li><li><b>09</b><em>Mi</em></li><li><b>10</b><em>Do</em></li><li><b>11</b><em>Fr</em></li><li class="r"><b>12</b><em>Sa</em></li><li class="r"><b>13</b><em>So</em></li>
    <li><b>14</b><em>Mo</em></li><li><b>15</b><em>Di</em></li><li><b>16</b><em>Mi</em></li><li><b>17</b><em>Do</em></li><li><b>18</b><em>Fr</em></li><li class="r"><b>19</b><em>Sa</em></li><li class="r"><b>20</b><em>So</em></li>
    <li><b>21</b><em>Mo</em></li><li><b>22</b><em>Di</em></li><li><b>23</b><em>Mi</em></li><li><b>24</b><em>Do</em></li><li><b>25</b><em>Fr</em></li><li class="r"><b>26</b><em>Sa</em></li><li class="r"><b>27</b><em>So</em><i>Ende der Sommerzeit</i></li>
    <li><b>28</b><em>Mo</em></li><li><b>29</b><em>Di</em></li><li><b>30</b><em>Mi</em></li><li class="r"><b>31</b><em>Do</em><i>Reformations­tag*</i></li>
  </ul>
  <ul class="month" style="left:894px">
    <li class="r"><b>01</b><em>Fr</em><i>Allerheiligen*</i></li><li class="r"><b>02</b><em>Sa</em><i>Allerseelen</i></li><li class="r"><b>03</b><em>So</em></li>
    <li><b>04</b><em>Mo</em></li><li><b>05</b><em>Di</em></li><li><b>06</b><em>Mi</em></li><li><b>07</b><em>Do</em></li><li><b>08</b><em>Fr</em></li><li class="r"><b>09</b><em>Sa</em></li><li class="r"><b>10</b><em>So</em></li>
    <li><b>11</b><em>Mo</em><i>St. Martin</i></li><li><b>12</b><em>Di</em></li><li><b>13</b><em>Mi</em></li><li><b>14</b><em>Do</em></li><li><b>15</b><em>Fr</em></li><li class="r"><b>16</b><em>Sa</em></li><li class="r"><b>17</b><em>So</em><i>Volks­trauertag</i></li>
    <li><b>18</b><em>Mo</em></li><li><b>19</b><em>Di</em></li><li class="r"><b>20</b><em>Mi</em><i>Buß- und Bettag*</i></li><li><b>21</b><em>Do</em></li><li><b>22</b><em>Fr</em></li><li class="r"><b>23</b><em>Sa</em></li><li class="r"><b>24</b><em>So</em><i>Totensonntag</i></li>
    <li><b>25</b><em>Mo</em></li><li><b>26</b><em>Di</em></li><li><b>27</b><em>Mi</em></li><li><b>28</b><em>Do</em></li><li><b>29</b><em>Fr</em></li><li class="r"><b>30</b><em>Sa</em></li>
  </ul>
  <ul class="month" style="left:978px">
    <li class="r"><b>01</b><em>So</em><i>1. Advent</i></li>
    <li><b>02</b><em>Mo</em></li><li><b>03</b><em>Di</em></li><li><b>04</b><em>Mi</em></li><li><b>05</b><em>Do</em></li><li><b>06</b><em>Fr</em><i>Nikolaus</i></li><li class="r"><b>07</b><em>Sa</em></li><li class="r"><b>08</b><em>So</em><i>2. Advent</i></li>
    <li><b>09</b><em>Mo</em></li><li><b>10</b><em>Di</em></li><li><b>11</b><em>Mi</em></li><li><b>12</b><em>Do</em></li><li><b>13</b><em>Fr</em></li><li class="r"><b>14</b><em>Sa</em></li><li class="r"><b>15</b><em>So</em><i>3. Advent</i></li>
    <li><b>16</b><em>Mo</em></li><li><b>17</b><em>Di</em></li><li><b>18</b><em>Mi</em></li><li><b>19</b><em>Do</em></li><li><b>20</b><em>Fr</em></li><li class="r"><b>21</b><em>Sa</em></li><li class="r"><b>22</b><em>So</em><i>4. Advent</i></li>
    <li><b>23</b><em>Mo</em></li><li><b>24</b><em>Di</em><i>Heiligabend</i></li><li class="r"><b>25</b><em>Mi</em><i>1. Weihnachts­feiertag</i></li><li class="r"><b>26</b><em>Do</em><i>2. Weihnachts­feiertag</i></li><li><b>27</b><em>Fr</em></li><li class="r"><b>28</b><em>Sa</em></li><li class="r"><b>29</b><em>So</em></li>
    <li><b>30</b><em>Mo</em></li><li><b>31</b><em>Di</em><i>Silvester</i></li>
  </ul>
  <ul class="month" style="left:1079px">
    <li class="r"><b>01</b><em>Mi</em><i>Neujahr</i></li><li><b>02</b><em>Do</em></li><li><b>03</b><em>Fr</em></li><li class="r"><b>04</b><em>Sa</em></li><li class="r"><b>05</b><em>So</em></li>
    <li class="r"><b>06</b><em>Mo</em><i>Heilige Drei Könige*</i></li><li><b>07</b><em>Di</em></li><li><b>08</b><em>Mi</em></li><li><b>09</b><em>Do</em></li><li><b>10</b><em>Fr</em></li><li class="r"><b>11</b><em>Sa</em></li><li class="r"><b>12</b><em>So</em></li>
    <li><b>13</b><em>Mo</em></li><li><b>14</b><em>Di</em></li><li><b>15</b><em>Mi</em></li><li><b>16</b><em>Do</em></li><li><b>17</b><em>Fr</em></li><li class="r"><b>18</b><em>Sa</em></li><li class="r"><b>19</b><em>So</em></li>
    <li><b>20</b><em>Mo</em></li><li><b>21</b><em>Di</em></li><li><b>22</b><em>Mi</em></li><li><b>23</b><em>Do</em></li><li><b>24</b><em>Fr</em></li><li class="r"><b>25</b><em>Sa</em></li><li class="r"><b>26</b><em>So</em></li>
    <li><b>27</b><em>Mo</em></li><li><b>28</b><em>Di</em></li><li><b>29</b><em>Mi</em></li><li><b>30</b><em>Do</em></li><li><b>31</b><em>Fr</em></li>
  </ul>

  <p class="note" style="left:39px">*Heilige Drei Könige: BW, BY, ST</p>
  <p class="note" style="left:464px">*Fronleichnam: BW, BY, HE, NW, RP, SL</p>
  <p class="note" style="left:634px">*Mariä Himmelfahrt: BY, SL</p>
  <p class="note" style="left:804px">*Reformationstag:<br>BB, HH, MV, NI, SH, SN, ST, TH</p>
  <p class="note" style="left:890px">*Allerheiligen: BW, BY, NW, RP, SL<br>*Buß- und Bettag: SN</p>
  <p class="note" style="left:1075px">*Heilige Drei Könige: BW, BY, ST</p>
</div>
</body>
</html>
```